Asia based real estate financing firm needs and AWESOME design for a biz card -Harbor Lending Circle

Looking for a stylish, & corporate-looking business card for a real estate financing brokerage firm in Asia, offering global mortgage loans. I uploaded our current logos. We would like to add a splash of color (perhaps the house icon) or any other suggestions are open. For the winning designer, we have a lot of work! Thanks and best of luck!

Target Market(s)

Real estate investors globally. We want to look more like a BANK and NOT a real estate company. Please don't play up on a "house" design.

Industry/Entity Type

Banking

Contact Information for Business Card

Harbor Lending Circle
Peter Wilks
Co-Founder | Partner

14 Cassia Lane, Suite 310
Singapore 047219
www.hlc-example.asia
peterwilks@hlc-example.asia
+65 555-0142
WeChat: peterwilks

Colors

Designer to choose colors to be used in the design.

Requirements
Must have
• Must have the standard business requirements for a card; name, address, email, etc
• Can be horizontal or vertical.
Nice to have
• It would be great to see some sort of variation to the logo with a pop of color. Red is good as we're in Asia, however, other options work as well.
• Our tag line is - Borderless mortgages. It doesn't have to be on the card but might be nice.
• I'd like to start seeing our tagline within the cards as well. - Borderless mortgages.
• Also, please add our location. The location for this card is Singapore so perhaps it can be highlighted or emphasised in some way.
• Singapore | Hong Kong | Shanghai | Manila
• As we will soon open an office in Shanghai, having an option for both languages would be great.
Should not have
• I'm exceited and open to your creativity ... knock it out of the park!

```html
<!DOCTYPE html>
<html lang="en">
<head>
<meta charset="utf-8">
<title>Harbor Lending Circle — Business Card</title>
<link href="https://fonts.googleapis.com/css2?family=Cinzel:wght@400;600&family=Tinos:wght@400&display=swap" rel="stylesheet">
<style>
  :root {
    --backdrop: #1e1e1f;
    --card-white: #ffffff;
    --ink: #111111;
    --accent-red: #c4242a;
    --accent-blue: #2a62b3;
    --grad-blue: #2f63b5;
    --grad-violet: #7a4f82;
    --grad-red: #d2363c;
    --rule: #222222;
    --sep: #888888;
  }
  * { box-sizing: border-box; margin: 0; padding: 0; }
  html, body { width: 1200px; height: 1200px; overflow: hidden; background: var(--backdrop); }
  .canvas { position: relative; width: 1200px; height: 1200px; }

  .card { position: absolute; left: 150px; width: 900px; height: 500px; overflow: hidden; }

  /* Back side */
  .card-back {
    top: 70px;
    background: linear-gradient(20deg, var(--grad-blue) 0%, var(--grad-violet) 38%, #a8474f 65%, var(--grad-red) 100%);
    color: #fff;
    text-align: center;
  }
  .card-back .brand-name {
    position: absolute; top: 170px; left: 0; right: 0;
    font-family: "Cinzel", serif; font-size: 50px; font-weight: 400; letter-spacing: 4px;
  }
  .card-back .web {
    position: absolute; top: 350px; left: 0; right: 0;
    font-family: "Tinos", serif; font-size: 19px; letter-spacing: 14px; text-transform: uppercase;
  }

  /* Front side */
  .card-front { top: 630px; background: var(--card-white); color: var(--ink); font-family: "Tinos", serif; }
  .card-front .brand-name {
    position: absolute; top: 70px; left: 70px;
    font-family: "Cinzel", serif; font-size: 44px; font-weight: 400; letter-spacing: 3px; color: var(--ink);
  }
  .person-name {
    position: absolute; top: 220px; left: 70px;
    font-family: "Cinzel", serif; font-weight: 600; font-size: 28px; letter-spacing: 1px;
  }
  .role {
    position: absolute; top: 232px; right: 60px;
    font-size: 22px; color: var(--accent-red);
  }
  .divider { position: absolute; top: 268px; left: 60px; right: 60px; height: 2px; background: var(--rule); }

  .contact-row {
    position: absolute; top: 292px; left: 66px; right: 60px;
    display: flex; justify-content: space-between; align-items: flex-start;
    font-size: 19px; line-height: 36px;
  }
  .contact-col { flex: none; }
  .contact-col.address { text-align: right; padding-top: 18px; }
  .contact-line { display: flex; align-items: center; gap: 12px; white-space: nowrap; }
  .contact-line svg { width: 19px; height: 19px; flex: none; }
  .col-sep { flex: none; width: 1px; height: 72px; background: var(--sep); }
  .col-sep.low { margin-top: 18px; }

  .base-band { position: absolute; left: 0; right: 0; bottom: 0; height: 30px; display: flex; }
  .base-band .red { flex: 0 0 52%; background: var(--accent-red); }
  .base-band .blue { flex: 1; background: var(--accent-blue); }
</style>
</head>
<body>
<main class="canvas">

  <section class="card card-back">
    <div class="brand-name">Harbor Lending Circle</div>
    <div class="web">www.hlc-example.asia</div>
  </section>

  <section class="card card-front">
    <div class="brand-name">Harbor Lending Circle</div>

    <div class="person-name">Peter Wilks</div>
    <div class="role">Co-Founder | Partner</div>
    <div class="divider"></div>

    <div class="contact-row">
      <div class="contact-col">
        <div class="contact-line">
          <svg viewBox="0 0 20 20" aria-hidden="true"><path fill="#c4242a" d="M3 7c0-3 14-3 14 0v2h-3V7.5H6V9H3z M5 10h10l2 7H3z"/></svg>
          <span>+65 555-0142</span>
        </div>
        <div class="contact-line">
          <svg viewBox="0 0 20 20" aria-hidden="true"><rect x="1.5" y="4" width="17" height="12" fill="none" stroke="#c4242a" stroke-width="2"/><path d="M2 5l8 6 8-6" fill="none" stroke="#c4242a" stroke-width="2"/></svg>
          <span>peterwilks@hlc-example.asia</span>
        </div>
      </div>

      <div class="col-sep"></div>

      <div class="contact-col">
        <div class="contact-line">
          <svg viewBox="0 0 20 20" aria-hidden="true"><g fill="none" stroke="#c4242a" stroke-width="1.6"><circle cx="10" cy="10" r="8"/><ellipse cx="10" cy="10" rx="3.5" ry="8"/><path d="M2 10h16M3.5 6h13M3.5 14h13"/></g></svg>
          <span>www.hlc-example.asia</span>
        </div>
        <div class="contact-line">
          <svg viewBox="0 0 20 20" aria-hidden="true"><circle cx="10" cy="10" r="8" fill="#c4242a"/></svg>
          <span>peterwilks</span>
        </div>
      </div>

      <div class="col-sep low"></div>

      <div class="contact-col address">
        <div>14 Cassia Lane, Suite 310</div>
        <div>Singapore 047219</div>
      </div>
    </div>

    <div class="base-band"><div class="red"></div><div class="blue"></div></div>
  </section>

</main>
</body>
</html>
```